Global Nano Technology Surface Protection company needs a new logo and cards

We are a Global company that will apply nanotechnology coatings on surfaces to prevent growth and spread of bacteria, viruses, mold etc. We deal with large corporates, airlines, hospitals and schools so we are after a new modern, simple and clean look that will have great visual impact.
We a company that is focused on prevention and protection.

Company name, Quorvane Systems Worldwide

Subtext, Antimicrobial Surface Protection

Logo, QVSW or QSW

Target Market(s)

Hospitals, Transport agencies, Airlines, Corporate entities

Industry/Entity Type

Protection

Contact Information for Business Card

Logo, QVSW or QSW
www.qvsw-example.us
Derek Holloway
+64290536218
tidyshieldnz@mailbox-example.com

Logo Text

QVSW

Requirements
Must have
• Simple clean look
Should not have
• Nothing too messy

```html
<!DOCTYPE html>
<html lang="en">
<head>
<meta charset="UTF-8">
<title>Quorvane Systems Worldwide – Business Card</title>
<link rel="stylesheet" href="https://fonts.googleapis.com/css2?family=Source+Sans+3:wght@400;600;700&display=swap">
<style>
  :root {
    --backdrop: #e4e4e4;
    --card: #f8f8f8;
    --ink: #2e2e30;
    --teal: #4cc5c9;
    --emblem-deep: #2f7fa8;
    --emblem-light: #a9d3e6;
  }
  * { margin: 0; padding: 0; box-sizing: border-box; }
  html, body {
    width: 1200px;
    height: 900px;
    overflow: hidden;
    background: var(--backdrop);
    font-family: "Source Sans 3", "Myriad Pro", sans-serif;
    color: var(--ink);
  }
  .card {
    position: absolute;
    left: 80px;
    top: 152px;
    width: 1040px;
    height: 596px;
    background: var(--card);
    box-shadow: 0 2px 6px rgba(0,0,0,0.12);
    text-align: center;
  }
  .brand-mark {
    position: absolute;
    top: 48px;
    left: 0;
    right: 0;
    font-weight: 700;
    font-size: 62px;
    line-height: 1;
    letter-spacing: 2px;
    color: var(--teal);
  }
  .company-name {
    position: absolute;
    top: 136px;
    left: 0;
    right: 0;
    font-weight: 700;
    font-size: 39px;
    line-height: 1.1;
  }
  .company-tagline {
    position: absolute;
    top: 182px;
    left: 0;
    right: 0;
    font-weight: 400;
    font-size: 32px;
    line-height: 1.1;
  }
  .person-name {
    position: absolute;
    top: 252px;
    left: 0;
    right: 0;
    font-weight: 400;
    font-size: 47px;
    line-height: 1.1;
  }
  .emblem-placeholder {
    position: absolute;
    top: 358px;
    left: 470px;
    width: 100px;
    height: 126px;
    border-radius: 8px;
    background: radial-gradient(circle at 50% 45%, var(--emblem-light), var(--emblem-deep));
    opacity: 0.85;
  }
  .contact-row {
    position: absolute;
    top: 527px;
    left: 0;
    right: 0;
    display: flex;
    justify-content: center;
    align-items: center;
    gap: 28px;
    font-size: 25px;
    line-height: 1;
  }
  .contact-item {
    display: flex;
    align-items: center;
    gap: 12px;
    white-space: nowrap;
  }
  .contact-icon {
    width: 34px;
    height: 34px;
    flex: none;
  }
</style>
</head>
<body>
  <main class="card">
    <div class="brand-mark">QVSW</div>
    <h1 class="company-name">Quorvane Systems Worldwide</h1>
    <p class="company-tagline">Antimicrobial Surface Protection</p>
    <p class="person-name">Derek Holloway</p>

    <div class="emblem-placeholder" role="img" aria-label="Protection emblem illustration: a crossed-out microbe inside a shield"></div>

    <div class="contact-row">
      <div class="contact-item">
        <svg class="contact-icon" viewBox="0 0 34 34" aria-hidden="true">
          <circle cx="17" cy="17" r="15.5" fill="none" stroke="var(--teal)" stroke-width="1.6"/>
          <path d="M11 9.5 l3 -0.5 l2 4.5 l-2 1.5 c1 2.5 3 4.5 5.5 5.5 l1.5 -2 l4.5 2 l-0.5 3 c-6 1 -14 -7 -14 -14 z" fill="var(--teal)"/>
        </svg>
        <span>+64290536218</span>
      </div>
      <div class="contact-item">
        <svg class="contact-icon" viewBox="0 0 34 34" aria-hidden="true">
          <circle cx="17" cy="17" r="15.5" fill="none" stroke="var(--teal)" stroke-width="1.6"/>
          <path d="M9 14 L17 8.5 L25 14 L25 24 L9 24 Z" fill="var(--teal)"/>
          <path d="M9 14 L17 20 L25 14" fill="none" stroke="#ffffff" stroke-width="1.4"/>
        </svg>
        <span>tidyshieldnz@mailbox-example.com</span>
      </div>
      <div class="contact-item">
        <svg class="contact-icon" viewBox="0 0 34 34" aria-hidden="true">
          <circle cx="17" cy="17" r="15.5" fill="none" stroke="var(--teal)" stroke-width="1.6"/>
          <g fill="none" stroke="var(--teal)" stroke-width="1.4">
            <circle cx="17" cy="17" r="9"/>
            <ellipse cx="17" cy="17" rx="4" ry="9"/>
            <line x1="8" y1="17" x2="26" y2="17"/>
            <line x1="9.5" y1="12.5" x2="24.5" y2="12.5"/>
            <line x1="9.5" y1="21.5" x2="24.5" y2="21.5"/>
          </g>
        </svg>
        <span>www.qvsw-example.us</span>
      </div>
    </div>
  </main>
</body>
</html>
```